依頼詳細
現在、既製品パッケージに入れて販売してますが、専用の袋を作りたいです。

盛り込むキーワード
◎商品名:はればれミックスナッツ
◎キャッチコピー:たべる時も、たべた後も、しあわせ。
◎無添加(無塩・無油)
◎葉月の膳ロゴ
◎リスが木の実を食べているイラスト

何種類かのパターンで販売するため、中身が見てわかるようにデザインしてほしいです。(面積で半分くらい透明部分になるように)
記載項目
袋サイズは、横210×縦310m
希望イメージ
シンプル 複雑
単色 カラフル
暗い 明るい
日常 高級
遊び心 厳粛
未来的 伝統的
女性的 男性的
希望する色
茶系、黄・オレンジ系
納品ファイル
• イラストレーター形式 (.ai)
• フォトショップ形式 (.psd)
もっと多くの作品を見たいので、5日間延長させていただきます。
■ 選んだ理由

森の動植物たちが、イメージにピッタリはまりました。

■ 提案者全員のお礼・コメント

今回初めてクラフタムを利用させていただきました。
短期間で非常に多くのご提案にビックリしましたし、また、その中から一つだけ選ぶのが大変でした。
今後も、引き続き商品パッケージの依頼をお願いすると思いますので、是非ご提案をよろしくお願いします。

```html
<!DOCTYPE html>
<html lang="ja">
<head>
<meta charset="utf-8">
<title>はればれミックスナッツ パッケージ</title>
<link href="https://fonts.googleapis.com/css2?family=Kiwi+Maru:wght@500&family=Zen+Maru+Gothic:wght@500;700&family=Shippori+Mincho:wght@700&display=swap" rel="stylesheet">
<style>
  :root {
    --cream: #fff8ec;
    --peach: #fbd9a6;
    --orange: #f3a24a;
    --title: #e2602a;
    --nut-light: #e9c79a;
    --nut-mid: #c58d58;
    --nut-dark: #8a5a35;
    --fur: #b89479;
    --ink: #4a2d1c;
    --white: #ffffff;
  }
  html, body { margin: 0; padding: 0; overflow: hidden; }
  .package {
    position: relative;
    width: 834px;
    height: 1200px;
    overflow: hidden;
    background: linear-gradient(180deg, var(--cream) 0%, var(--peach) 22%, var(--orange) 48%, var(--nut-light) 62%);
    font-family: "Zen Maru Gothic", sans-serif;
    color: var(--ink);
  }
  .nuts-photo {
    position: absolute;
    left: 0; top: 560px;
    width: 834px; height: 640px;
    background:
      radial-gradient(circle at 20% 40%, var(--nut-light) 0 14%, transparent 30%),
      radial-gradient(circle at 75% 60%, var(--nut-light) 0 12%, transparent 28%),
      linear-gradient(180deg, rgba(197,141,88,0) 0%, var(--nut-mid) 18%, var(--nut-dark) 100%);
  }
  .flower {
    position: absolute;
    border-radius: 50%;
    background: var(--white);
    opacity: .9;
  }
  .product-name {
    position: absolute;
    left: 0; top: 70px;
    width: 834px;
    margin: 0;
    text-align: center;
    font-family: "Kiwi Maru", serif;
    font-weight: 500;
    color: var(--title);
    line-height: 1.3;
  }
  .product-name .lead { display: block; font-size: 76px; letter-spacing: 4px; }
  .product-name .main { display: block; font-size: 92px; letter-spacing: 2px; }
  .squirrel {
    position: absolute;
    left: 270px; top: 350px;
    width: 360px; height: 430px;
    border-radius: 46% 46% 40% 40%;
    background: linear-gradient(180deg, var(--fur), #9b7558);
  }
  .catch-copy {
    position: absolute;
    left: 24px; top: 425px;
    margin: 0;
    font-size: 32px;
    font-weight: 700;
    line-height: 1.35;
    text-shadow: 0 0 6px var(--white), 0 0 10px var(--white), 0 0 14px var(--white);
  }
  .additive-free {
    position: absolute;
    left: 630px; top: 455px;
    width: 190px;
    text-align: center;
    font-weight: 700;
    text-shadow: 0 0 6px var(--white), 0 0 10px var(--white);
  }
  .additive-free .headline { display: block; font-size: 36px; }
  .additive-free .detail { display: block; font-size: 27px; margin-top: 8px; }
  .brand-plate {
    position: absolute;
    left: 180px; top: 1040px;
    width: 475px; height: 128px;
    border-radius: 16px;
    background: var(--white);
    text-align: center;
  }
  .brand-plate .brand-name {
    display: block;
    margin-top: 16px;
    font-family: "Shippori Mincho", serif;
    font-size: 52px;
    font-weight: 700;
    letter-spacing: 6px;
    color: var(--ink);
  }
  .brand-plate .brand-roman {
    display: block;
    margin-top: 4px;
    font-family: "Shippori Mincho", serif;
    font-size: 17px;
    font-weight: 700;
    letter-spacing: 4px;
    color: var(--ink);
  }
</style>
</head>
<body>
<main class="package">
  <div class="nuts-photo" role="img" aria-label="ミックスナッツ(アーモンド、カシューナッツ、くるみ)の写真"></div>

  <div class="flower" style="left:28px;top:18px;width:92px;height:92px" role="img" aria-label="白い花の飾り"></div>
  <div class="flower" style="left:690px;top:20px;width:62px;height:62px" role="img" aria-label="白い花の飾り"></div>
  <div class="flower" style="left:740px;top:100px;width:64px;height:64px" role="img" aria-label="白い花の飾り"></div>
  <div class="flower" style="left:640px;top:115px;width:80px;height:80px" role="img" aria-label="白い花の飾り"></div>
  <div class="flower" style="left:40px;top:170px;width:66px;height:66px" role="img" aria-label="白い花の飾り"></div>
  <div class="flower" style="left:550px;top:370px;width:72px;height:72px" role="img" aria-label="白い花の飾り"></div>
  <div class="flower" style="left:20px;top:560px;width:62px;height:62px" role="img" aria-label="白い花の飾り"></div>
  <div class="flower" style="left:735px;top:640px;width:62px;height:62px" role="img" aria-label="白い花の飾り"></div>
  <div class="flower" style="left:70px;top:955px;width:62px;height:62px" role="img" aria-label="白い花の飾り"></div>
  <div class="flower" style="left:680px;top:960px;width:62px;height:62px" role="img" aria-label="白い花の飾り"></div>
  <div class="flower" style="left:40px;top:1110px;width:56px;height:56px" role="img" aria-label="白い花の飾り"></div>
  <div class="flower" style="left:720px;top:1120px;width:56px;height:56px" role="img" aria-label="白い花の飾り"></div>

  <h1 class="product-name">
    <span class="lead">はればれ</span>
    <span class="main">ミックスナッツ</span>
  </h1>

  <div class="squirrel" role="img" aria-label="木の実をくわえたリスのイラスト"></div>

  <p class="catch-copy">たべる時も、<br>たべた後も、<br>しあわせ。</p>

  <div class="additive-free">
    <span class="headline">無添加</span>
    <span class="detail">( 無塩・無油 )</span>
  </div>

  <div class="brand-plate">
    <span class="brand-name">葉月の膳</span>
    <span class="brand-roman">HAZUKI NO ZEN</span>
  </div>
</main>
</body>
</html>
```